Canvassing technical expertise for co-ownerships

Good morning,
The KORBA company specializes in real estate expertise. We would like to create a flyer to attract new customers. Our main target is condominium trustees and co-ownerships.
We want a double-sided A4 format. The language used must be French. The flyer must come as close as possible to the graphic charter of our website (title font “brandon grotesque”; text font “avenir light”; green color code “#2A7C6F”, beige “#FFFDF8”, possibly with the following nuances in the theme: #95BDB6; #2C8D7E). The site is accessible at the following address: https://www.korba-expertise.example/.
Our logo must be accompanied by the phrase “Experts at the service of co-ownership!”.
The flyer must convey the main information from the website, emphasizing:
- All the missions offered (see “Our services” page of the website)
- We operate throughout the French national territory, with teams spread across the territory.
- A short text about our history (“about” page of the site)
- Making contact, by email contact@saskorba.example or by telephone 06.71.28.94.07.

Our postal address should appear more discreetly at the bottom of the page, in the form “SAS KORBA, 58 Rue des Tilleuls Verts, 34 700 LUNEL”

Target Market(s)

Condominium associations and co-ownerships

Industry/Entity Type

Expertise du bâtiment

Font styles to use
Other font styles liked:
• police titres « brandon grotesque » ; police texte « avenir light »

Colors

Designer to choose colors to be used in the design.

Requirements
Must have
• All the characteristics requested in the project description. The language used must be French.
Nice to have
• A neat and serious general appearance
Should not have
• Not intended to be entertaining, funny, too colorful, etc.

```html
<!DOCTYPE html>
<html lang="fr">
<head>
<meta charset="utf-8">
<title>KORBA – Flyer recto verso</title>
<link rel="stylesheet" href="https://fonts.googleapis.com/css2?family=Jost:wght@300;400;500;600;700&family=Nunito+Sans:wght@300;400;600&display=swap">
<style>
:root{
  --green:#2A7C6F;
  --green-2:#2C8D7E;
  --green-soft:#95BDB6;
  --beige:#FFFDF8;
  --bg:#c3c3c3;
  --panel:#e4e4e4;
  --grey-bar:#7a7a7a;
  --ink:#222;
  --title:"Jost",sans-serif;
  --text:"Nunito Sans",sans-serif;
}
*{margin:0;padding:0;box-sizing:border-box}
html,body{width:1200px;height:2854px;overflow:hidden}
body{background:var(--bg);position:relative;font-family:var(--text);color:var(--ink)}
.page{position:absolute;left:171px;width:857px;height:1213px;background:#fff;overflow:hidden;box-shadow:0 6px 14px rgba(0,0,0,.35)}
.page--front{top:160px}
.page--back{top:1475px}
.abs{position:absolute}
.photo{position:absolute}
.framed{border:3px solid var(--green);background:#fff;padding:5px}
.framed .fill{width:100%;height:100%}

/* logo */
.logo-square{left:46px;top:32px;width:70px;height:70px;background:var(--green)}
.logo-name{left:130px;top:28px;font-family:var(--title);font-weight:500;font-size:70px;line-height:80px;color:var(--green);letter-spacing:4px}
.tagline{left:45px;top:150px;font-family:var(--text);font-weight:600;font-size:13.5px;color:#222}

/* hero */
.hero-photo{left:401px;top:43px;width:413px;height:398px}
.hero-panel{left:45px;top:198px;width:429px;height:274px;background:var(--green);color:#fff;padding:26px 18px 0 18px}
.hero-fold{left:474px;top:441px;width:0;height:0;border-top:31px solid var(--green);border-right:23px solid transparent}
.hero-panel .light{font-family:var(--title);font-weight:300;font-size:27px;letter-spacing:4.6px;line-height:31px}
.hero-panel .mid{font-family:var(--title);font-weight:500;font-size:25px;line-height:30px}
.hero-panel .big{font-family:var(--title);font-weight:600;font-size:38px;line-height:42px}
.hero-panel .dots{display:flex;gap:4px;margin:14px 0 16px 2px}
.hero-panel .dots span{width:7px;height:7px;background:#fff}
.hero-panel p{font-family:var(--title);font-size:17.5px;line-height:25px}

/* story blocks */
.band{background:var(--panel);z-index:2}
.band h3{font-family:var(--title);font-weight:500;color:var(--green);font-size:16.5px;line-height:22.5px;margin-bottom:6px}
.band p{font-size:14.5px;line-height:19px;color:#222}
.band-1{left:45px;top:486px;width:774px;height:227px}
.band-1 .accent{left:0;top:0;width:362px;height:214px;background:var(--green)}
.band-1 .photo{left:16px;top:14px;width:344px;height:200px}
.band-1 .copy{left:390px;top:12px;width:374px}
.band-2{left:45px;top:733px;width:774px;height:227px}
.band-2 .accent{right:0;top:0;width:16px;height:227px;background:var(--green)}
.band-2 .photo{left:410px;top:12px;width:349px;height:202px}
.band-2 .copy{left:22px;top:12px;width:380px}

.crew-photo{left:0;top:928px;width:440px;height:285px;z-index:1;background:linear-gradient(90deg,#9a8a78,#c8b4a0 45%,#e6e6e6 85%,#fff)}

/* contact */
.contact{position:absolute;left:443px;width:414px;z-index:3}
.contact h4{position:absolute;left:0;top:0;font-family:var(--title);font-weight:500;font-size:20.5px;color:var(--green);white-space:nowrap}
.contact .row{position:absolute;display:flex;align-items:center;gap:10px;font-size:13.5px}
.contact .addr{position:absolute;left:182px;top:32px;display:flex;gap:10px;font-size:13.5px;line-height:17px}
.contact svg{flex:none}
.contact .web{position:absolute;left:3px;top:85px;width:411px;height:28px;background:var(--grey-bar);color:#fff;font-family:var(--title);font-weight:600;font-size:20px;letter-spacing:3.4px;line-height:28px;padding-left:14px;white-space:nowrap}
.contact .note{position:absolute;left:5px;top:128px;width:370px;font-size:11.5px;line-height:15.5px}

/* back */
.plans-photo{left:45px;top:55px;width:771px;height:298px}
.services-title{left:176px;top:390px;width:483px;height:45px;background:#6d6d6d;color:#fff;font-family:var(--title);font-weight:600;font-size:27px;line-height:45px;text-align:center;border-radius:3px;box-shadow:0 4px 4px rgba(0,0,0,.3)}
.services-intro{left:45px;top:447px;width:771px;text-align:center;font-size:21px;line-height:26px}
.cards{left:47px;top:523px;width:764px;display:grid;grid-template-columns:repeat(4,176px);column-gap:22px;row-gap:21px}
.card{height:196px;background:var(--green);border-radius:0 0 8px 8px;overflow:hidden;display:flex;flex-direction:column}
.card.tall{height:202px}
.card .thumb{height:108px;border:2px solid #fff;border-bottom:none}
.card .label{flex:1;display:flex;align-items:center;justify-content:center;text-align:center;color:#fff;font-family:var(--title);font-size:18px;line-height:22px;padding:0 6px}
.tower-photo{left:0;top:980px;width:434px;height:233px;background:linear-gradient(160deg,#fff 10%,#8b96a3 50%,#2f3944 100%)}
</style>
</head>
<body>

<section class="page page--front">
  <div class="abs logo-square"></div>
  <div class="abs logo-name">KORBA</div>
  <div class="abs tagline">DES EXPERTS AU SERVICE DE LA COPROPRIÉTÉ !</div>

  <div class="photo framed hero-photo"><div class="fill" role="img" aria-label="Immeuble résidentiel moderne à façade blanche et bleue sous un ciel nuageux" style="background:linear-gradient(160deg,#dfe8f0 20%,#7fa8d4 55%,#2a3d55)"></div></div>
  <div class="abs hero-panel">
    <div class="light">PARTENAIRE DE</div>
    <div class="mid">CONFIANCE DES SYNDICATS</div>
    <div class="big">DE COPROPRIÉTÉ ET</div>
    <div class="light">DES COPROPRIÉTAIRES</div>
    <div class="dots"><span></span><span></span><span></span><span></span><span></span></div>
    <p>Fondée en 2019, KORBA joue un rôle essentiel sur l’ensemble des enjeux techniques des copropriétés.</p>
  </div>
  <div class="abs hero-fold"></div>

  <div class="abs band band-1">
    <div class="abs accent"></div>
    <div class="photo" role="img" aria-label="Expert en casque de chantier et cliente examinant un document devant une maison" style="background:linear-gradient(120deg,#cfd6d8,#b8a8a8 50%,#5e6b52)"></div>
    <div class="abs copy">
      <h3>Chez KORBA, nous offrons un accompagnement technique complet aux syndics de copropriété et aux copropriétaires</h3>
      <p>en apportant une expertise pointue sur le bâti et en les soutenant à chaque étape de leur projet. Avec aujourd'hui un réseau de plus d'une soixantaine de collaborateurs, nous sommes fiers de proposer une gamme complète de services spécialisés pour assister nos clients dans les étapes clés de la vie de leur immeuble.</p>
    </div>
  </div>

  <div class="abs band band-2">
    <div class="abs accent"></div>
    <div class="photo" role="img" aria-label="Couple recevant les clés de leur logement des mains d’un agent" style="background:linear-gradient(110deg,#a89a8a,#d8c8b8 50%,#3a3a40)"></div>
    <div class="abs copy">
      <h3>Avec une présence&nbsp; nationale notre équipe de plus d’une soixantaine d’intervenants est prête à répondre à vos besoins, où que vous soyez. »</h3>
      <p>Chez KORBA, nous sommes animés par la passion de fournir des solutions sur mesure et de qualité à nos clients. Nous nous engageons à être à l'écoute de leurs besoins et à leur offrir un service irréprochable à chaque étape de leur parcours avec nous.</p>
    </div>
  </div>

  <div class="photo crew-photo" role="img" aria-label="Trois ingénieurs en casques et gilets orange étudiant des plans sur un chantier"></div>

  <div class="contact" style="top:993px">
    <h4>Contactez-nous pour plus d’informations</h4>
    <div class="row" style="left:3px;top:38px"><svg width="13" height="13" viewBox="0 0 13 13"><rect width="13" height="13" rx="2" fill="var(--green)"/><path d="M4 3l1.4 0 .6 1.8-.9.7a5 5 0 0 0 2.4 2.4l.7-.9 1.8.6V9a1 1 0 0 1-1 1A6 6 0 0 1 3 4a1 1 0 0 1 1-1z" fill="#fff"/></svg>06 71 28 94 07</div>
    <div class="row" style="left:3px;top:65px"><svg width="13" height="13" viewBox="0 0 13 13"><rect width="13" height="13" rx="2" fill="var(--green)"/><rect x="3" y="4" width="7" height="5" fill="#fff"/><path d="M3 4l3.5 3L10 4" stroke="var(--green)" fill="none"/></svg>contact@saskorba.example</div>
    <div class="addr"><svg width="13" height="13" viewBox="0 0 13 13"><rect width="13" height="13" rx="2" fill="var(--green)"/><path d="M6.5 2.5a2.7 2.7 0 0 1 2.7 2.7c0 2-2.7 5-2.7 5s-2.7-3-2.7-5a2.7 2.7 0 0 1 2.7-2.7z" fill="#fff"/><circle cx="6.5" cy="5.2" r="1" fill="var(--green)"/></svg><span>SAS KORBA,<br>58 Rue des Tilleuls Verts,<br>34 700 LUNEL</span></div>
    <div class="web">www.korba-expertise.example</div>
    <p class="note">Nous intervenons sur tout le territoire national français, avec des équipes réparties sur tout le territoire.</p>
  </div>
</section>

<section class="page page--back">
  <div class="photo framed plans-photo"><div class="fill" role="img" aria-label="Mains d’ingénieurs travaillant sur des plans avec une tablette, un casque jaune et une règle" style="background:linear-gradient(120deg,#c9ccd0,#eef0f2 45%,#b9bdc2)"></div></div>
  <div class="abs services-title">LES SERVICES QUE NOUS OFFRONS</div>
  <p class="abs services-intro">Nous voudrions aussi présenter les prestations que nous proposons et<br>qui sont les suivantes :</p>

  <div class="abs cards">
    <div class="card"><div class="thumb" role="img" aria-label="Technicien en casque remplissant un formulaire" style="background:linear-gradient(135deg,#aab6c4,#d9a86a)"></div><div class="label">Assistance à<br>la livraison</div></div>
    <div class="card"><div class="thumb" role="img" aria-label="Visite d’un logement avec un agent" style="background:linear-gradient(135deg,#b8a890,#4a4e58)"></div><div class="label">Visite<br>d’immeuble</div></div>
    <div class="card"><div class="thumb" role="img" aria-label="Calcul sur documents avec calculatrice" style="background:linear-gradient(135deg,#e8e8ea,#8d8f96)"></div><div class="label">Audit de<br>garantie<br>décennale</div></div>
    <div class="card"><div class="thumb" role="img" aria-label="Ouvriers en casques examinant des plans" style="background:linear-gradient(135deg,#e0a040,#3d6aa0)"></div><div class="label">Assistance<br>technique garantie<br>décennale</div></div>
    <div class="card tall"><div class="thumb" role="img" aria-label="Table couverte de notes colorées et de plans" style="background:linear-gradient(135deg,#d8c0a8,#e890b0)"></div><div class="label">PPT Plan<br>Pluriannuel de<br>Travaux</div></div>
    <div class="card tall"><div class="thumb" role="img" aria-label="Équipe en casques vue du dessus autour de plans" style="background:linear-gradient(135deg,#50703a,#e0c040)"></div><div class="label">Expertise privée<br>Audit technique<br>du bâti</div></div>
    <div class="card tall"><div class="thumb" role="img" aria-label="Expert présentant un diagnostic à une cliente" style="background:linear-gradient(135deg,#dcdcdc,#3a4048)"></div><div class="label">Diagnostic de<br>performance<br>énergétique (DPE)</div></div>
    <div class="card tall"><div class="thumb" role="img" aria-label="Inspecteur consultant une tablette sur un chantier" style="background:linear-gradient(135deg,#b0a070,#2e3440)"></div><div class="label">Suivi des levées de<br>réserves et de la<br>garantie de parfait<br>achèvement</div></div>
  </div>

  <div class="photo tower-photo" role="img" aria-label="Gratte-ciels vus en contre-plongée"></div>

  <div class="contact" style="top:993px">
    <h4>Contactez-nous pour plus d’informations</h4>
    <div class="row" style="left:3px;top:38px"><svg width="13" height="13" viewBox="0 0 13 13"><rect width="13" height="13" rx="2" fill="var(--green)"/><path d="M4 3l1.4 0 .6 1.8-.9.7a5 5 0 0 0 2.4 2.4l.7-.9 1.8.6V9a1 1 0 0 1-1 1A6 6 0 0 1 3 4a1 1 0 0 1 1-1z" fill="#fff"/></svg>06 71 28 94 07</div>
    <div class="row" style="left:3px;top:65px"><svg width="13" height="13" viewBox="0 0 13 13"><rect width="13" height="13" rx="2" fill="var(--green)"/><rect x="3" y="4" width="7" height="5" fill="#fff"/><path d="M3 4l3.5 3L10 4" stroke="var(--green)" fill="none"/></svg>contact@saskorba.example</div>
    <div class="addr"><svg width="13" height="13" viewBox="0 0 13 13"><rect width="13" height="13" rx="2" fill="var(--green)"/><path d="M6.5 2.5a2.7 2.7 0 0 1 2.7 2.7c0 2-2.7 5-2.7 5s-2.7-3-2.7-5a2.7 2.7 0 0 1 2.7-2.7z" fill="#fff"/><circle cx="6.5" cy="5.2" r="1" fill="var(--green)"/></svg><span>SAS KORBA,<br>58 Rue des Tilleuls Verts,<br>34 700 LUNEL</span></div>
    <div class="web">www.korba-expertise.example</div>
    <p class="note">Nous intervenons sur tout le territoire national français, avec des équipes réparties sur tout le territoire.</p>
  </div>
</section>

</body>
</html>
```